Web Design Project + Development

We need a web design for a new company called Vireltan Group.
We are a young, financial company with a professional but playful culture.
I have attached the company logo.
I need design and development for this web site.
See below for site map
Landing Page
(Should have two tabs in the middle to lead into Vireltan Trading or Vireltan Capital)
Landing Page for Vireltan Trading
Welcome Page
Tabs on the top are (Home/About Us/FAQ/Careers/Contact Us)
Landing Page for Vireltan Capital
Welcome Page
Please submit design of landing pages ONLY.
Contents of the web site will be supplied after we select designer.
Look and feel of this website should be simple, crisp and professional but keeping to the brand logo, font and colours
Industry/Entity Type
Financial
Requirements
Must have
- please see below website of our desired look and feel.
http://www.qorbafunds.com.au/campaign/smsf/overview

```html
<!DOCTYPE html>
<html lang="en">
<head>
<meta charset="utf-8">
<title>Vireltan Group</title>
<link href="https://fonts.googleapis.com/css2?family=Carlito:wght@400;700&display=swap" rel="stylesheet">
<style>
:root{
  --blue:#4aa3df;
  --blue-light:#6cc0f2;
  --hero:#43a4e0;
  --dark:#3b4045;
  --page:#f0f0f0;
  --text:#8a8a8a;
  --heading:#444;
  --nav:#555;
  --btn-grey:#8e8e8e;
  --white:#fff;
}
*{margin:0;padding:0;box-sizing:border-box}
html,body{width:1200px;height:1069px;overflow:hidden}
body{font-family:"Carlito",sans-serif;background:var(--page);position:relative}
.abs{position:absolute}
.header{left:0;top:0;width:1200px;height:149px;background:var(--white)}
.brand{left:246px;top:72px;display:flex;align-items:center;gap:10px}
.brand-dot{width:36px;height:36px;border-radius:50%;background:var(--blue)}
.brand-name{font-size:34px;font-weight:700;color:var(--dark);letter-spacing:.5px}
.search{left:773px;top:75px;width:185px;height:19px;background:#ececec;border:1px solid #e0e0e0;font-size:7px;color:#c4c4c4;padding:5px 6px}
.search svg{position:absolute;right:5px;top:4px}
.nav{top:110px;left:634px;display:flex;font-size:15px;color:var(--nav)}
.nav a{color:inherit;text-decoration:none}
.nav .active{color:var(--blue)}
.hero{left:0;top:149px;width:1200px;height:294px;background:var(--hero)}
.hero-title{left:252px;top:194px;color:var(--white);line-height:1;font-weight:400}
.hero-title .l1{font-size:48px;display:block;letter-spacing:.5px}
.hero-title .l2{font-size:34px;display:block;margin-top:4px;margin-left:-1px}
.hero-btn{left:321px;top:298px;width:178px;height:30px;background:var(--blue-light);color:var(--white);font-size:14px;text-align:center;line-height:30px;box-shadow:0 3px 0 #3b8fc4}
.video{left:606px;top:184px;width:346px;height:177px;background:linear-gradient(180deg,#ffffff,#fbf3dc);box-shadow:0 14px 14px -8px rgba(0,0,0,.5)}
.video svg{position:absolute;left:153px;top:66px}
.signup{left:239px;top:405px;width:719px;height:84px;background:var(--dark);border-radius:3px}
.signup-label{left:19px;top:24px;line-height:.92;font-weight:700;color:var(--white);font-size:19px}
.signup-label span{display:block;color:var(--blue);font-weight:400}
.signup-input{left:200px;top:25px;width:351px;height:36px;background:var(--white);border:1px solid #ccc;font-size:9px;color:#999;padding:12px}
.signup-btn{left:557px;top:25px;width:123px;height:37px;background:var(--blue);color:var(--white);font-size:17px;font-weight:700;text-align:center;line-height:37px;border-radius:2px}
.col-title{font-size:26px;color:var(--heading);top:508px;font-weight:400}
.col-title span{color:var(--blue)}
.rule{top:546px;height:1px;background:#e2e2e2}
.pic-left{left:336px;top:562px;width:224px;height:150px;background:linear-gradient(135deg,#d6edbd,#a6d46e)}
.pic-right{left:668px;top:559px;width:283px;height:169px;background:linear-gradient(135deg,#071525,#0f4686 55%,#1b66b8)}
.copy{top:756px;font-size:12.5px;line-height:18px;color:var(--text);text-align:justify}
.read-more{top:925px;width:127px;height:30px;background:var(--btn-grey);color:var(--white);font-size:13px;text-align:center;line-height:30px}
.footer{left:0;top:982px;width:1200px;height:87px;background:var(--dark)}
.social{top:28px;width:28px;height:28px;border-radius:50%;background:var(--white)}
.foot-nav{left:429px;top:28px;font-size:10px;color:var(--white);display:flex}
.foot-nav .sep{margin:0 26px}
.foot-copy{left:489px;top:48px;font-size:10px;color:var(--white)}
</style>
</head>
<body>
<header class="header abs">
  <div class="brand abs"><div class="brand-dot"></div><div class="brand-name">vireltan</div></div>
  <div class="search abs">Type search
    <svg width="10" height="10" viewBox="0 0 10 10"><circle cx="4" cy="4" r="3" fill="none" stroke="#888"/><line x1="6.2" y1="6.2" x2="9" y2="9" stroke="#888" stroke-width="1.4"/></svg>
  </div>
  <nav class="nav abs">
    <a class="active" style="margin-right:21px">Home</a>
    <a style="margin-right:18px">About Us</a>
    <a style="margin-right:24px">FAQ</a>
    <a style="margin-right:18px">Careers</a>
    <a>Contact Us</a>
  </nav>
</header>

<section class="hero abs"></section>
<h1 class="hero-title abs"><span class="l1">Vireltan</span><span class="l2">Trading + Capital</span></h1>
<div class="hero-btn abs">FOR MORE DETAILS</div>
<div class="video abs" role="img" aria-label="Video still: savings piggy bank tied with a gift ribbon">
  <svg width="40" height="46" viewBox="0 0 40 46"><polygon points="2,2 38,23 2,44" fill="#c8c8c8"/></svg>
</div>

<section class="signup abs">
  <div class="signup-label abs">SIGN UP FOR OUR<span>EMAIL NEWSLETTER</span></div>
  <div class="signup-input abs">Enter the e-mail Address</div>
  <div class="signup-btn abs">SIGN UP NOW</div>
</section>

<h2 class="col-title abs" style="left:248px">Welcome to <span>Vireltan</span></h2>
<div class="rule abs" style="left:248px;width:404px"></div>
<div class="pic-left abs" role="img" aria-label="Illustration of green and blue radial charts joined by lines"></div>
<p class="copy abs" style="left:248px;width:404px">At vero eos et accusamus et iusto odio dignissimos ducimus qui blanditiis praesentium voluptatum deleniti atque corrupti quos dolores et quas molestias excepturi sint occaecati cupiditate non provident, similique sunt in culpa qui officia deserunt mollitia animi, id est laborum et dolorum fuga. Et harum quidem rerum facilis est et expedita distinctio. Nam libero tempore, cum soluta nobis est eligendi optio cumque nihil impedit quo minus id quod maxime placeat facere possimus, omnis voluptas assumenda est, omnis dolor repellendus.</p>
<div class="read-more abs" style="left:523px">Read More</div>

<h2 class="col-title abs" style="left:667px">What <span>We Offer</span></h2>
<div class="rule abs" style="left:667px;width:285px"></div>
<div class="pic-right abs" role="img" aria-label="Photo of a stock market board with a rising chart"></div>
<p class="copy abs" style="left:666px;width:284px">At vero eos et accusamus et iusto odio dignissimos ducimus qui blanditiis praesentium voluptatum deleniti atque corrupti quos dolores et quas molestias excepturi sint occaecati cupiditate non provident, similique sunt in culpa qui officia deserunt mollitia animi, id est laborum et dolorum fuga. Et harum quidem rerum facilis est et expedita distinctio. Nam libero tempore, cum soluta nobis est eligendi optio cumque nihil .</p>
<div class="read-more abs" style="left:822px">Read More</div>

<footer class="footer abs">
  <div class="social abs" style="left:249px"></div>
  <div class="social abs" style="left:287px"></div>
  <div class="social abs" style="left:325px"></div>
  <div class="foot-nav abs">
    <span>Home</span><span class="sep">|</span><span>About Us</span><span class="sep">|</span><span>FAQ</span><span class="sep">|</span><span>Careers</span><span class="sep">|</span><span>Contact Us</span>
  </div>
  <div class="foot-copy abs">Copyright 2000-2013,Vireltan ,All rights reserved</div>
</footer>
</body>
</html>
```